My Insurance Agency Show Display

I need to design a 10 ft x 8 ft backdrop for a show display. This is a pop up fabric most likely display that will be used for a show booth. I need someone to design something more attractive with my logo and make it more flashy so people can see and remember my company. I have attached my rough design so far. I would like it to look more modern. The photo in the design does not have to be used.

This is for an insurance agency that provides Home, Auto, Life and Health products to consumers. We also provide Renters insurance, Commercial, RV, mobile homes, and other products to our customers.

Target Market(s)

Home Owners, and Multiple Auto Owners

Industry/Entity Type

Property and Causality Insurance

Font styles to use
Sans Serif

Colors
0054AA
0677BA
7BADD7
CADEEF
E8F1F8
00AB8E
00BBA5
67D7C9
C6EFE9
E9F9F6

Requirements
Must have
• Attractive Modern Layout
Nice to have
• new and creative. Something that pops with color
Should not have
• Any affiliation to other insurance agencies.

```html
<!DOCTYPE html>
<html lang="en">
<head>
<meta charset="utf-8">
<title>Brightpath Insurance Agency – Show Backdrop</title>
<link rel="stylesheet" href="https://fonts.googleapis.com/css2?family=Montserrat:wght@800;900&family=Saira+Semi+Condensed:wght@500;600&family=Saira+Condensed:wght@700&family=Roboto:wght@400&display=swap">
<style>
  :root {
    --stage: #eef1f5;
    --lavender: #c9cdf6;
    --white: #ffffff;
    --blue: #1d3fe0;
    --blue-deep: #0054aa;
    --green: #3ddc7e;
    --teal: #67d7c9;
    --teal-soft: #c6efe9;
    --teal-mist: #e9f9f6;
    --ink: #1b1b24;
    --magenta: #d6166e;
    --photo-warm: #b7a28c;
    --photo-dark: #3c3a3c;
  }
  * { margin: 0; padding: 0; box-sizing: border-box; }
  html, body { width: 1200px; height: 450px; overflow: hidden; background: var(--stage); }

  .backdrop {
    position: absolute; left: 319px; top: 0;
    width: 562px; height: 450px; overflow: hidden;
    background: linear-gradient(180deg, var(--lavender) 0%, #e7e9fb 30%, var(--white) 55%);
  }
  .backdrop__shapes { position: absolute; inset: 0; }

  .brand {
    position: absolute; left: 0; width: 356px; top: 26px;
    text-align: center; color: var(--ink);
    font-family: "Saira Semi Condensed", sans-serif; font-weight: 600;
  }
  .brand__mark {
    display: block; width: 40px; height: 40px; margin: 0 auto 14px;
    background: var(--magenta); border-radius: 4px;
  }
  .brand__name { font-size: 21px; line-height: 22px; letter-spacing: 0.5px; }
  .brand__sub { font-size: 16px; line-height: 20px; letter-spacing: 4px; }

  .headline {
    position: absolute; left: 29px; top: 140px;
    font-family: "Montserrat", sans-serif; font-weight: 900;
    line-height: 35px; color: var(--blue);
  }
  .headline__lead { color: var(--green); font-size: 41px; letter-spacing: -0.3px; display: block; }
  .headline__line { font-size: 35px; display: block; }
  .headline__accent { color: var(--green); }

  .coverage {
    position: absolute; top: 266px; list-style: none;
    font-family: "Saira Semi Condensed", sans-serif; font-weight: 500;
    font-size: 15.5px; line-height: 15px; color: var(--ink);
  }
  .coverage li::before { content: "+"; color: var(--teal); font-weight: 600; margin-right: 5px; }
  .coverage--main { left: 37px; }
  .coverage--more { left: 177px; }

  .intro {
    position: absolute; left: 29px; top: 368px; width: 258px;
    font-family: "Roboto", sans-serif; font-size: 8px; line-height: 11px; color: var(--ink);
  }
  .phone {
    position: absolute; left: 297px; top: 365px;
    font-family: "Saira Condensed", sans-serif; font-weight: 700;
    font-size: 42px; line-height: 48px; color: var(--magenta); letter-spacing: 0.5px;
  }
  .footer-band {
    position: absolute; left: 0; bottom: 0; width: 100%; height: 9px;
    background: linear-gradient(90deg, var(--teal-soft), var(--teal), var(--lavender));
  }
</style>
</head>
<body>
<main class="backdrop">
  <svg class="backdrop__shapes" width="562" height="450" viewBox="0 0 562 450">
    <defs>
      <linearGradient id="tealHex" x1="0" y1="0" x2="0" y2="1">
        <stop offset="0" stop-color="#a9c9f0"/>
        <stop offset="1" stop-color="#67d7c9"/>
      </linearGradient>
      <linearGradient id="photoTone" x1="0" y1="0" x2="1" y2="1">
        <stop offset="0" stop-color="#3c3a3c"/>
        <stop offset="0.5" stop-color="#b7a28c"/>
        <stop offset="1" stop-color="#e6d2c0"/>
      </linearGradient>
    </defs>
    <!-- top-left streaks -->
    <g stroke-linecap="round">
      <line x1="20" y1="-4" x2="48" y2="26" stroke="#67d7c9" stroke-width="6"/>
      <line x1="58" y1="-6" x2="108" y2="40" stroke="#67d7c9" stroke-width="7"/>
      <line x1="98" y1="-6" x2="120" y2="14" stroke="#9bb0ee" stroke-width="6"/>
    </g>
    <!-- faint background tiles -->
    <g fill="#e9f9f6">
      <rect x="335" y="240" width="34" height="34" rx="8"/>
      <rect x="372" y="290" width="34" height="34" rx="8"/>
      <rect x="296" y="300" width="30" height="30" rx="7"/>
      <rect x="460" y="330" width="34" height="34" rx="8"/>
    </g>
    <!-- hexagon frame -->
    <polygon points="368,66 482,0 600,66 600,262 488,326 368,262" fill="url(#tealHex)" opacity="0.85"/>
    <polygon points="362,58 480,-8 600,58 600,214 488,280 362,210" fill="none" stroke="#ffffff" stroke-width="1.5"/>
    <polygon role="img" aria-label="Photo of a smiling young family: mother, father and two small children at home"
      points="372,64 482,2 600,64 600,206 488,272 372,204" fill="url(#photoTone)" stroke="#1d3fe0" stroke-width="4"/>
  </svg>

  <header class="brand">
    <span class="brand__mark"></span>
    <div class="brand__name">BRIGHTPATH INSURANCE</div>
    <div class="brand__sub">AGENCY</div>
  </header>

  <h1 class="headline">
    <span class="headline__lead">PROTECHTING</span>
    <span class="headline__line">WHAT MATTERS</span>
    <span class="headline__line">MOST TO <span class="headline__accent">YOU</span></span>
  </h1>

  <ul class="coverage coverage--main">
    <li>HOME</li>
    <li>COMMERCIAL</li>
    <li>UMBRELLA</li>
    <li>RV</li>
    <li>HEALTH &amp; OTHER PRODUCTS</li>
  </ul>
  <ul class="coverage coverage--more">
    <li>RENTERS</li>
    <li>AUTO</li>
    <li>MOBILE HOMES</li>
    <li>LIFE</li>
  </ul>

  <p class="intro">Our comprehensive insurance services provide you with peace of mind, encuring that your assets, health, and loved onese are safeguarded against unforeseen circumstances. Trust in our expertise to navigate the complexities of insurance and secure a brighter future for you and your family.</p>

  <p class="phone">555-014-0272</p>
  <div class="footer-band"></div>
</main>
</body>
</html>
```